Lena Corvell Business Card

I need a business card that reflects my current website: itslenacorvell.example and screenshot attached. If we keep the color scheme of the site and sample card below that would be ideal. The business card should include the information on the attached sample cards.

Industry/Entity Type

Business

```html
<!DOCTYPE html>
<html lang="en">
<head>
<meta charset="utf-8">
<title>Lena Corvell Business Card</title>
<link rel="stylesheet" href="https://fonts.googleapis.com/css2?family=Kaushan+Script&family=Oswald:wght@300&display=swap">
<style>
  :root {
    --backdrop: #2b2b2b;
    --card-white: #ffffff;
    --card-mist: #ececec;
    --teal: #5cc3b0;
    --teal-deep: #4fb3a1;
    --ink: #111111;
    --on-teal: #ffffff;
    --photo-warm: #8a4a2e;
    --photo-cool: #9db4c8;
  }
  * { margin: 0; padding: 0; box-sizing: border-box; }
  html, body {
    width: 1200px; height: 1000px; overflow: hidden;
    background: var(--backdrop);
  }
  .stage {
    position: relative; width: 1200px; height: 1000px;
    display: flex; align-items: center; justify-content: center;
  }
  .business-card {
    position: relative; width: 904px; height: 550px;
    background: linear-gradient(180deg, var(--card-white) 0%, var(--card-mist) 55%);
    overflow: hidden;
    box-shadow: 0 10px 30px rgba(0,0,0,0.5);
    font-family: "Oswald", sans-serif; font-weight: 300;
  }
  .portrait {
    position: absolute; left: 632px; top: 10px; width: 250px; height: 320px;
    background: radial-gradient(ellipse at 50% 35%, var(--photo-warm) 0%, #5a2e1c 42%, var(--photo-cool) 78%, var(--card-mist) 100%);
    border-radius: 50% 50% 8% 8% / 42% 42% 8% 8%;
  }
  .card-shapes { position: absolute; inset: 0; width: 904px; height: 550px; }
  .wordmark {
    position: absolute; left: 46px; top: 146px;
    font-size: 58px; line-height: 70px; color: var(--ink);
    letter-spacing: 1px; white-space: nowrap;
  }
  .identity { position: absolute; left: 32px; top: 344px; color: var(--on-teal); }
  .identity-name {
    font-family: "Kaushan Script", cursive; font-weight: 400;
    font-size: 44px; line-height: 50px; margin-bottom: 2px;
  }
  .identity-role { font-size: 30px; line-height: 42px; white-space: nowrap; }
  .divider {
    position: absolute; left: 446px; top: 344px; width: 3px; height: 178px;
    background: var(--on-teal);
  }
  .contact-list {
    position: absolute; right: 20px; top: 350px; list-style: none;
    color: var(--on-teal); font-size: 30px; line-height: 42px; text-align: right;
  }
  .contact-list li { display: flex; justify-content: flex-end; align-items: center; gap: 12px; white-space: nowrap; }
  .contact-icon { width: 26px; height: 26px; flex: none; }
  .social-mark { width: 22px; height: 22px; border-radius: 50%; background: var(--on-teal); flex: none; margin: 0 2px; }
</style>
</head>
<body>
<main class="stage">
  <article class="business-card">
    <div class="portrait" role="img" aria-label="Smiling portrait photo of Lena Corvell in a denim jacket"></div>

    <svg class="card-shapes" viewBox="0 0 904 550" aria-hidden="true">
      <path d="M0 266 Q 450 318 904 274 L 904 282 Q 450 330 0 292 Z" fill="var(--ink)"/>
      <path d="M0 292 Q 450 330 904 282 L 904 550 L 0 550 Z" fill="var(--teal)"/>
    </svg>

    <div class="wordmark">iam Lena Corvell</div>

    <section class="identity">
      <h1 class="identity-name">Lena Corvell</h1>
      <p class="identity-role">Brand Curator</p>
      <p class="identity-role">Digital Storyteller</p>
      <p class="identity-role">Social Entrprenuer</p>
    </section>

    <div class="divider"></div>

    <ul class="contact-list">
      <li>me@lenacorvell.example
        <svg class="contact-icon" viewBox="0 0 26 26" aria-hidden="true"><rect x="2" y="6" width="22" height="15" fill="none" stroke="#fff" stroke-width="2"/><path d="M2 6 L13 15 L24 6" fill="none" stroke="#fff" stroke-width="2"/></svg>
      </li>
      <li>555.010.4821
        <svg class="contact-icon" viewBox="0 0 26 26" aria-hidden="true"><path d="M4 10 Q13 2 22 10 L19 13 L16 10 L10 10 L7 13 Z" fill="none" stroke="#fff" stroke-width="2"/><rect x="6" y="14" width="14" height="8" rx="2" fill="none" stroke="#fff" stroke-width="2"/></svg>
      </li>
      <li>@itslenacorvell <span class="social-mark"></span></li>
      <li>itslenacorvell.example
        <svg class="contact-icon" viewBox="0 0 26 26" aria-hidden="true"><circle cx="13" cy="13" r="10" fill="none" stroke="#fff" stroke-width="2"/><ellipse cx="13" cy="13" rx="4.5" ry="10" fill="none" stroke="#fff" stroke-width="2"/><path d="M3 13 H23" stroke="#fff" stroke-width="2"/></svg>
      </li>
    </ul>
  </article>
</main>
</body>
</html>
```